Original and Visually striking member badge Business Card

I'm a real estate agent in the Richmond (VA) area. I'd like something that stands out from the cliche realtor business card. I want it to look nice.

My two taglines are as follows and you can use either or both... perhaps one on the front, one on the back. Whatever looks best.

1. Upbeat. Warm. Here for YOU.
and
2. YOU are the most important person.

Thank you for your input.
Updates

Your designs and creativity are great so far. I just found out from my supervising broker that I need to include 2 small realtor logos (the one with the R - KPT and the Equal Housing one.) They can be quite small. I added a few other pictures to choose from too. Thank you all for your excellent work.

Target Market(s)

home buyers and home sellers

Industry/Entity Type

Real Estate

Contact Information for Business Card

Lorna Vatch, Sales Agent
Upbeat. Warm. Here for YOU.
Coltrane Realtors OVK®
20417 E Maple Ave #300, Larkmoor, VA 20999
www.findyourdoorstep.example
lorna.vatch@mailbox.example
(804) 555-0142 office
(804) 555-0187 cell

Requirements
Must have
• Ok.. so I definitely need a picture of myself and I've included a few to choose from. And my company logo. I would like my picture to be the central image, larger than the company logo. The other pictures are some recognizable landmarks in Richmond (not necessary, but just wanted you to have some choices)

I need to have the realtor logo (R) with the KPT as well as the Equal Housing logo (they can be small.)

Double sided please

Should not have
• nothing cheesy or too cliche please

```html
<!DOCTYPE html>
<html lang="en">
<head>
<meta charset="utf-8">
<title>Lorna Vatch – Business Card</title>
<link rel="stylesheet" href="https://fonts.googleapis.com/css2?family=Bebas+Neue&family=Open+Sans:wght@300;400&display=swap">
<style>
  :root {
    --ink: #222222;
    --text: #3a3a3a;
    --muted: #666666;
    --sky: #5bc8e2;
    --paper: #ffffff;
    --frame: #444444;
    --photo-dark: #2f3634;
    --photo-mid: #4a524f;
  }
  * { box-sizing: border-box; margin: 0; padding: 0; }
  html, body { width: 1200px; height: 1000px; overflow: hidden; background: var(--paper); }
  .canvas {
    position: relative; width: 1200px; height: 1000px;
    border: 2px solid var(--frame); background: var(--paper);
    font-family: "Open Sans", Arial, sans-serif; color: var(--text);
  }

  /* Front side */
  .card-front {
    position: absolute; left: 114px; top: 174px; width: 700px; height: 384px;
    background: var(--paper); border: 1.5px solid var(--frame);
    transform: rotate(-8.5deg);
  }
  .portrait {
    position: absolute; left: 21px; top: 42px; width: 306px; height: 306px;
    border-radius: 50%; border: 2px solid var(--ink);
    background: radial-gradient(circle at 48% 42%, var(--photo-mid), var(--photo-dark) 70%);
  }
  .greeting {
    position: absolute; left: 380px; top: 28px; width: 178px; height: 38px;
    background: var(--sky); border-radius: 7px;
    color: var(--paper); font: 400 25px/38px Arial, Helvetica, sans-serif; text-align: center;
  }
  .greeting-tail { position: absolute; left: 350px; top: 60px; width: 100px; height: 62px; }
  .intro { position: absolute; left: 430px; top: 112px; font-size: 25px; font-weight: 300; color: var(--ink); }
  .agent-name {
    position: absolute; left: 434px; top: 152px;
    font-family: "Bebas Neue", Impact, sans-serif; font-size: 35px; font-weight: 400; line-height: 1; color: var(--ink);
  }
  .agent-role { position: absolute; left: 438px; top: 188px; font-size: 17px; font-weight: 300; color: var(--text); }
  .badges { position: absolute; left: 580px; top: 305px; display: flex; gap: 4px; align-items: flex-end; }
  .badge-member { width: 38px; height: 48px; background: var(--ink); }
  .badge-listing { width: 56px; height: 38px; border: 2px solid var(--ink); background: var(--paper); }
  .tagline { position: absolute; left: 590px; top: 357px; font-size: 8px; color: var(--muted); white-space: nowrap; }

  /* Back side */
  .card-back {
    position: absolute; left: 488px; top: 535px; width: 624px; height: 342px;
    background: var(--paper); border: 1.5px solid var(--ink); overflow: hidden;
  }
  .badge-housing { position: absolute; left: 74px; top: 48px; width: 120px; height: 116px; background: var(--ink); }
  .contact-list { position: absolute; left: 326px; top: 44px; list-style: none; }
  .contact-list li { display: flex; align-items: flex-start; font-size: 18px; font-weight: 300; line-height: 25px; margin-bottom: 7.5px; }
  .contact-list svg { width: 14px; height: 16px; margin: 4px 14px 0 0; flex: none; }
  .website { position: absolute; left: 14px; top: 248px; display: flex; align-items: center; font-size: 20px; font-weight: 300; }
  .website svg { width: 16px; height: 16px; margin-right: 22px; }
  .wave { position: absolute; left: 0; bottom: 0; width: 624px; height: 342px; }
</style>
</head>
<body>
<div class="canvas">

  <section class="card-front">
    <div class="portrait" role="img" aria-label="Portrait photo of Lorna Vatch"></div>
    <svg class="greeting-tail" viewBox="0 0 100 62"><polygon points="40,0 80,0 0,62" fill="#5bc8e2"/></svg>
    <div class="greeting">Hello</div>
    <p class="intro">I’m,</p>
    <h1 class="agent-name">Lorna Vatch</h1>
    <p class="agent-role">Sales Agent</p>
    <div class="badges">
      <div class="badge-member" role="img" aria-label="Professional association member badge"></div>
      <div class="badge-listing" role="img" aria-label="KPT listing service badge"></div>
    </div>
    <p class="tagline">Upbeat. Warm. Here for YOU</p>
  </section>

  <section class="card-back">
    <div class="badge-housing" role="img" aria-label="Fair housing badge"></div>
    <ul class="contact-list">
      <li><svg viewBox="0 0 14 16"><rect x="3" y="1" width="8" height="14" rx="1.5" fill="none" stroke="#5bc8e2" stroke-width="1.4"/><line x1="5.5" y1="12.5" x2="8.5" y2="12.5" stroke="#5bc8e2" stroke-width="1.2"/></svg>(804) 555-0187</li>
      <li><svg viewBox="0 0 14 16"><path d="M3 2 L5.5 2 L6.5 5 L5 6.5 C5.8 8.8 7.2 10.2 9.5 11 L11 9.5 L14 10.5 L14 13 C8 14 2 8 3 2 Z" fill="#5bc8e2"/></svg>(804) 555-0142</li>
      <li><svg viewBox="0 0 14 16"><rect x="1" y="4" width="12" height="9" fill="none" stroke="#5bc8e2" stroke-width="1.2"/><polyline points="1,4 7,9 13,4" fill="none" stroke="#5bc8e2" stroke-width="1.2"/></svg>lorna.vatch@mailbox.example</li>
      <li><svg viewBox="0 0 14 16"><path d="M7 1 C3.5 1 1.5 3.5 1.5 6 C1.5 9.5 7 15 7 15 C7 15 12.5 9.5 12.5 6 C12.5 3.5 10.5 1 7 1 Z" fill="#5bc8e2"/><circle cx="7" cy="6" r="2" fill="#fff"/></svg><span>Coltrane Realtors OVK®<br>20417 E Maple Ave #300,<br>Larkmoor, VA 20999</span></li>
    </ul>
    <p class="website"><svg viewBox="0 0 16 16"><circle cx="8" cy="8" r="6.5" fill="none" stroke="#5bc8e2" stroke-width="1.2"/><ellipse cx="8" cy="8" rx="3" ry="6.5" fill="none" stroke="#5bc8e2" stroke-width="1"/><line x1="1.5" y1="8" x2="14.5" y2="8" stroke="#5bc8e2" stroke-width="1"/></svg>www.findyourdoorstep.example</p>
    <svg class="wave" viewBox="0 0 624 342" aria-hidden="true">
      <path d="M0,342 L0,318 C120,335 300,338 440,312 C520,296 580,250 624,203 L624,342 Z" fill="#000"/>
    </svg>
  </section>

</div>
</body>
</html>
```